Food Safety 1-California workers only

3.25" by 4.5" Black and White Magazine Ad
This ad is to train California workers only.
Workers will be trained on: Food Safety, FSMA (Food Safety Modernization Act), using equipment safety, food processing production skills, worker safety, supervisory skills, communication skills.
"FREE TRAINING", The company does the training or Harbor Learning will provide the training.
Training grants range from $100,000 to $400,000.
Companies must be in business for profit.
Companies must train 200 employees or more.
This program is for California workers only.
Incumbent or new-hires are eligible.

Target Market(s)

California food processors, farms, food packaging, food processors, companies under FSMA, food safety, food production who need to train employees.

Industry/Entity Type

Food Production

Font styles to use
Serif
Sans Serif

Colors

Designer to choose colors to be used in the design.

Requirements
Must have
• This is a 3.25 inch by 4.5 inch magazine ad. It must be black and white. No color.
• The deliverable must be in basic PhotoShop. The ad does not need to include any graphics and be text only if needed. If you have a black and white graphic that will show well.
• Look at www.BQXFoodSafety..com
• Use the text from "FOOD2U-Photoshop-052018" file as your starting point.
Nice to have
• A black and white graphic about food. See www.BQXFoodSafety.com
Should not have
• No color.

```html
<!DOCTYPE html>
<html lang="en">
<head>
<meta charset="utf-8">
<title>Harbor Learning – California Training Ad</title>
<link rel="stylesheet" href="https://fonts.googleapis.com/css2?family=Jost:wght@400;500;700;800&display=swap">
<style>
  :root {
    --stage: #a7a8aa;
    --ink: #000000;
    --paper: #ffffff;
    --bar: #9a9a9a;
  }
  * { margin: 0; padding: 0; box-sizing: border-box; }
  html, body { width: 909px; height: 1200px; overflow: hidden; }
  body {
    background: var(--stage);
    font-family: "Jost", "Futura", sans-serif;
    position: relative;
  }
  .ad {
    position: absolute;
    left: 134px; top: 157px;
    width: 640px; height: 885px;
    background: var(--ink);
    color: var(--paper);
    box-shadow: 0 14px 30px rgba(0,0,0,0.35);
  }
  .topic {
    position: absolute; left: 0; width: 100%;
    text-align: center; line-height: 1;
  }
  .topic--fsma {
    top: 50px; font-size: 22px; font-weight: 500;
    display: flex; align-items: center; justify-content: center; gap: 10px;
    padding: 0 71px;
  }
  .topic--fsma .rule { flex: 1; height: 1px; background: var(--paper); }
  .topic--skills { top: 80px; font-size: 26px; font-weight: 500; }
  .headline-frame { position: absolute; left: 69px; top: 100px; overflow: visible; }
  .qualify-bar, .contact-bar {
    position: absolute; left: 69px; width: 504px;
    background: var(--bar); color: var(--ink);
    text-align: center; line-height: 1;
  }
  .qualify-bar { top: 520px; height: 22px; font-size: 18px; font-weight: 700; padding-top: 2px; }
  .contact-bar { top: 744px; height: 25px; font-size: 20px; font-weight: 500; padding-top: 3px; }
  .contact-bar strong { font-weight: 700; }
  .requirements {
    position: absolute; left: 69px; top: 551px; width: 504px;
    list-style: none; font-size: 20px; font-weight: 500; line-height: 26.5px;
  }
  .requirements li {
    display: flex; align-items: center; gap: 4px; text-align: center;
  }
  .requirements li::before, .requirements li::after {
    content: ""; flex: 1; border-top: 1px dotted var(--paper); margin-top: 2px;
  }
  .requirements li.continued::before, .requirements li.continued::after { border-color: transparent; }
  .company {
    position: absolute; left: 0; top: 771px; width: 100%; height: 77px;
    background: var(--paper); color: var(--ink);
    text-align: center; font-size: 19.5px; font-weight: 500; font-style: normal; line-height: 21px;
    padding-top: 8px;
  }
  .reach {
    position: absolute; left: 0; top: 855px; width: 100%;
    display: flex; justify-content: center; gap: 22px;
    font-size: 20px; font-weight: 700; line-height: 1;
  }
  .reach span { display: flex; align-items: center; gap: 5px; }
</style>
</head>
<body>
  <article class="ad">
    <p class="topic topic--fsma"><span class="rule"></span>FSMA<span class="rule"></span></p>
    <p class="topic topic--skills">PRODUCTION SKILLS</p>

    <svg class="headline-frame" width="504" height="410" viewBox="0 0 504 410" aria-labelledby="hl">
      <title id="hl">Worker safety – You do the training, the State of California pays for it!</title>
      <rect x="2.5" y="22.5" width="499" height="385" fill="none" stroke="#fff" stroke-width="5"/>
      <rect x="13.5" y="34.5" width="477" height="361" fill="none" stroke="#fff" stroke-width="3"/>
      <rect x="112" y="14" width="280" height="30" fill="#000"/>
      <text x="252" y="39" text-anchor="middle" font-family="Jost, sans-serif" font-weight="700" font-size="29" fill="#fff">WORKER SAFETY</text>
      <g font-family="Jost, sans-serif" fill="#fff">
        <text x="41" y="126" font-weight="400" font-size="74" textLength="424" lengthAdjust="spacingAndGlyphs">YOU DO THE</text>
        <text x="41" y="196" font-weight="800" font-size="82" textLength="424" lengthAdjust="spacingAndGlyphs">TRAINING</text>
        <text x="41" y="263" font-weight="800" font-size="74" textLength="424" lengthAdjust="spacingAndGlyphs">THE STATE OF</text>
        <text x="41" y="327" font-weight="800" font-size="74" textLength="424" lengthAdjust="spacingAndGlyphs">CALIFORNIA</text>
        <text x="41" y="392" font-weight="800" font-size="74" textLength="424" lengthAdjust="spacingAndGlyphs">PAYS FOR IT!</text>
      </g>
    </svg>

    <h2 class="qualify-bar">HOW TO QUALIFY</h2>
    <ul class="requirements">
      <li>TRAIN CALIFORNIA WORKERS ONLY.</li>
      <li>TRAINEES MUST EARN $15/HOUR</li>
      <li>FULL-TIME WORKERS ONLY.</li>
      <li>EMPLOYEES MUST ATTEND AT LEAST 8 HOURS</li>
      <li class="continued">OR TRAINING</li>
      <li>YOU MUST TRAIN 200 OR MORE EMPLOYEES</li>
      <li>SEASONAL WORKERS ARE ELIGIBLE</li>
    </ul>

    <p class="contact-bar">CONTACT <strong>DANIEL BROOKS</strong></p>

    <address class="company">
      HARBOR LEARNING, Inc.,1200 HARBOR VIEW<br>
      DRIVE, SUITE 410, IRVINE, CA 92614<br>
      WWW.HARBORLEARNCA.COM&nbsp; WWW.BQXFOODSAFETY.COM
    </address>

    <p class="reach">
      <span>
        <svg width="16" height="16" viewBox="0 0 16 16" aria-hidden="true"><circle cx="8" cy="8" r="7" fill="none" stroke="#fff" stroke-width="2"/><rect x="4" y="5" width="8" height="6" fill="#fff"/><path d="M4 5l4 3.5L12 5" fill="none" stroke="#000" stroke-width="1"/></svg>
        DAN.BROOKS@HARBORLEARNCA.COM
      </span>
      <span>
        <svg width="16" height="16" viewBox="0 0 16 16" aria-hidden="true"><circle cx="8" cy="8" r="8" fill="#fff"/><path d="M5 4c-1 1-1 3 1 5.5S10 13 11.5 12l.5-1.5-2-1.2-1 .8C8 9.5 6.5 8 6.2 7l.8-1-1.2-2z" fill="#000"/></svg>
        (949)555-0147
      </span>
    </p>
  </article>
</body>
</html>
```